Dune Air & Plus business card

I need an awesome, double-sided business card designed with our new logo. I would like the one side black with the colored logo, and the back side is all yours. I'd like to see horizontal and vertical layouts. Get creative! Thank you.

Target Market(s)

HVAC, Heating and Cooling in Phoenix, AZ

Industry/Entity Type

HVAC

Contact Information for Business Card

We need our new logo on the card. Tom Harker, (623) 555-0142, tom@trydunesair.com, www.trydunesair.com, ROC 514273

```html
<!DOCTYPE html>
<html lang="en">
<head>
<meta charset="utf-8">
<title>Dune Air &amp; Plus — Business Card</title>
<link href="https://fonts.googleapis.com/css2?family=Libre+Franklin:wght@400;500;600;800&display=swap" rel="stylesheet">
<style>
  :root {
    --stage: #e9e9e9;
    --card-black: #05080a;
    --card-white: #ffffff;
    --ink: #111111;
    --brand-blue: #2f7fd6;
    --brand-orange: #f08a24;
    --shade: #1a1c1e;
    --soft-text: #f2f2f2;
  }
  * { box-sizing: border-box; margin: 0; padding: 0; }
  html, body { width: 1152px; height: 1200px; overflow: hidden; }
  body {
    background: var(--stage);
    font-family: "Libre Franklin", Arial, sans-serif;
    display: flex;
    flex-direction: column;
    align-items: center;
    justify-content: center;
    gap: 60px;
  }
  .card {
    position: relative;
    width: 900px;
    height: 514px;
    overflow: hidden;
    box-shadow: 0 6px 24px rgba(0,0,0,.18);
  }

  /* Front */
  .card--front { background: var(--card-black); }
  .front__illustration {
    position: absolute;
    left: 80px; top: 180px;
    width: 740px; height: 296px;
    border-radius: 60px 60px 0 0;
    background: linear-gradient(180deg, var(--shade) 0%, #0c0e10 100%);
  }
  .front__brand {
    position: absolute;
    left: 0; right: 0; top: 220px;
    display: flex; align-items: center; justify-content: center; gap: 18px;
  }
  .brand-dot {
    width: 34px; height: 34px; border-radius: 50%;
    background: var(--brand-orange);
  }
  .front__name {
    font-weight: 800;
    font-size: 56px;
    letter-spacing: 1px;
    color: var(--brand-blue);
  }
  .front__web {
    position: absolute;
    left: 0; right: 0; top: 424px;
    text-align: center;
    font-size: 17px;
    font-weight: 500;
    color: var(--soft-text);
    text-transform: uppercase;
  }

  /* Back */
  .card--back { background: var(--card-white); color: var(--ink); }
  .back__brand {
    position: absolute;
    left: 60px; width: 250px; top: 240px;
    text-align: center;
    font-weight: 800;
    font-size: 26px;
    line-height: 1.15;
    color: var(--ink);
  }
  .back__divider {
    position: absolute;
    left: 366px; top: 124px;
    width: 1.5px; height: 266px;
    background: var(--ink);
  }
  .back__person {
    position: absolute;
    left: 512px; top: 146px;
    font-size: 46px;
    font-weight: 600;
  }
  .contact {
    position: absolute;
    left: 465px; top: 232px;
    list-style: none;
  }
  .contact__item {
    display: flex; align-items: center; gap: 16px;
    height: 47px;
    font-size: 30px;
  }
  .contact__icon { width: 30px; height: 30px; flex: none; }
</style>
</head>
<body>

  <section class="card card--front" aria-label="Card front">
    <div class="front__illustration" role="img" aria-label="Faint illustration of a three-bay garage building behind the logo"></div>
    <div class="front__brand">
      <span class="brand-dot"></span>
      <span class="front__name">Dune Air &amp; Plus</span>
    </div>
    <p class="front__web">www.trydunesair.com</p>
  </section>

  <section class="card card--back" aria-label="Card back">
    <p class="back__brand">Dune Air &amp; Plus</p>
    <div class="back__divider"></div>
    <h1 class="back__person">Tom Harker</h1>
    <ul class="contact">
      <li class="contact__item">
        <svg class="contact__icon" viewBox="0 0 30 30" aria-hidden="true">
          <circle cx="15" cy="15" r="14" fill="#111"/>
          <path d="M10 8.5l3 .2 1.2 3.6-1.8 1.4a9 9 0 0 0 4 4l1.4-1.8 3.6 1.2.2 3c-5.5 1.2-12.8-6.1-11.6-11.6z" fill="#fff"/>
        </svg>
        <span>(623) 555-0142</span>
      </li>
      <li class="contact__item">
        <svg class="contact__icon" viewBox="0 0 30 30" aria-hidden="true">
          <circle cx="15" cy="15" r="4.5" fill="none" stroke="#111" stroke-width="2.6"/>
          <path d="M19.5 11v5.5c0 2 3.5 2 3.5-1.5A8 8 0 1 0 19 22" fill="none" stroke="#111" stroke-width="2.6" stroke-linecap="round"/>
        </svg>
        <span>tom@trydunesair.com</span>
      </li>
      <li class="contact__item">
        <svg class="contact__icon" viewBox="0 0 30 30" aria-hidden="true">
          <circle cx="15" cy="15" r="14" fill="#111"/>
          <path d="M15 7a6 6 0 0 0-6 6c0 4.5 6 10 6 10s6-5.5 6-10a6 6 0 0 0-6-6z" fill="#fff"/>
          <circle cx="15" cy="13" r="2.3" fill="#111"/>
        </svg>
        <span>ROC 514273</span>
      </li>
    </ul>
  </section>

</body>
</html>
```